Business Card for my New Brokerage

Looking to get a business card design for my new Real Estate Brokerage.
I want it with Picture, Phone Number, Email, Website, Office Address
Name and Designation. Please add logo too.

Target Market(s)

Real Estate Investors or Home Buyers

Industry/Entity Type

Real Estate

Contact Information for Business Card

Name, Email, Phone Number, website, email, office address

Colors
EB3D1F
EC4F4E
F09395
F8D3D4
FCEDEE

Requirements
Must have
• Minimalistic, Clean, Modern, Photo
Nice to have
• White and Red Colors

```html
<!DOCTYPE html>
<html lang="en">
<head>
<meta charset="utf-8">
<title>Ember Realty Co — Business Card</title>
<link rel="stylesheet" href="https://fonts.googleapis.com/css2?family=Montserrat:wght@600;700&family=Arimo:wght@400&display=swap">
<style>
  :root {
    --red: #d8000f;
    --red-edge: #c4000c;
    --ink: #3a3a3a;
    --muted: #6f6f6f;
    --paper: #ffffff;
    --pale: #ececec;
    --charcoal: #2a2a2c;
    --charcoal-light: #3e3e41;
    --backdrop: #e6e6e4;
  }
  * { box-sizing: border-box; margin: 0; padding: 0; }
  html, body { width: 1200px; height: 801px; overflow: hidden; }
  body {
    background: var(--backdrop);
    font-family: "Arimo", Arial, sans-serif;
    position: relative;
  }
  .card {
    position: absolute;
    top: 252px;
    width: 525px;
    height: 300px;
    border-bottom: 5px solid var(--red-edge);
    overflow: hidden;
  }
  .card-front { left: 55px; background: var(--paper); }
  .card-back { left: 620px; background: var(--charcoal); }

  .watermark {
    position: absolute;
    right: 40px;
    top: 30px;
    width: 200px;
    height: 200px;
    border-radius: 50%;
    background: var(--pale);
  }
  .brand {
    position: absolute;
    left: 36px;
    top: 46px;
    font-family: "Montserrat", sans-serif;
    font-weight: 700;
    color: var(--red);
  }
  .brand-name { font-size: 34px; letter-spacing: 1px; line-height: 1; }
  .brand-sub { font-size: 13px; letter-spacing: 6px; margin-top: 6px; margin-left: 60px; }

  .person { position: absolute; left: 128px; top: 150px; }
  .person-name {
    font-family: "Montserrat", sans-serif;
    font-weight: 700;
    font-size: 16px;
    color: var(--red);
    letter-spacing: 0.3px;
  }
  .person-title { font-size: 14px; color: var(--ink); margin-top: 2px; }

  .contacts { position: absolute; left: 128px; top: 208px; list-style: none; }
  .contacts li {
    display: flex; align-items: center; gap: 9px;
    font-size: 14px; color: var(--ink); line-height: 22px;
  }
  .contacts svg { width: 13px; height: 13px; fill: var(--red); flex: none; }

  .address {
    position: absolute;
    right: 36px;
    top: 235px;
    font-size: 13px;
    color: var(--ink);
    text-align: right;
    line-height: 17px;
  }

  .pattern {
    position: absolute; inset: 0;
    background: linear-gradient(120deg, var(--charcoal) 0%, var(--charcoal) 45%, var(--charcoal-light) 100%);
  }
  .back-brand {
    position: absolute;
    right: 40px;
    top: 138px;
    font-family: "Montserrat", sans-serif;
    font-weight: 700;
    font-size: 20px;
    color: var(--red);
    letter-spacing: 1px;
  }
</style>
</head>
<body>
  <section class="card card-front">
    <div class="watermark" aria-hidden="true"></div>
    <div class="brand">
      <div class="brand-name">EMBER</div>
      <div class="brand-sub">REALTY CO</div>
    </div>
    <div class="person">
      <div class="person-name">DANIEL HARPER</div>
      <div class="person-title">Manager</div>
    </div>
    <ul class="contacts">
      <li>
        <svg viewBox="0 0 24 24" aria-hidden="true"><path d="M6.6 10.8a15.1 15.1 0 0 0 6.6 6.6l2.2-2.2a1 1 0 0 1 1-.25 11.4 11.4 0 0 0 3.6.57 1 1 0 0 1 1 1V20a1 1 0 0 1-1 1A17 17 0 0 1 3 4a1 1 0 0 1 1-1h3.5a1 1 0 0 1 1 1c0 1.25.2 2.45.57 3.6a1 1 0 0 1-.25 1z"/></svg>
        123-555-0140
      </li>
      <li>
        <svg viewBox="0 0 24 24" aria-hidden="true"><path d="M2 5h20v14H2z M2 5l10 8 10-8" fill="none" stroke="#d8000f" stroke-width="2.4"/></svg>
        hello@emberrealty.co
      </li>
      <li>
        <svg viewBox="0 0 24 24" aria-hidden="true"><circle cx="12" cy="12" r="9" fill="none" stroke="#d8000f" stroke-width="2.4"/><path d="M3 12h18M12 3c3 3 3 15 0 18M12 3c-3 3-3 15 0 18" fill="none" stroke="#d8000f" stroke-width="1.8"/></svg>
        www.emberrealty.co
      </li>
    </ul>
    <div class="address">210 Maple Row, Fairview<br>ST, ZIP 00000</div>
  </section>

  <section class="card card-back">
    <div class="pattern" role="img" aria-label="Embossed repeating brand pattern in dark grey"></div>
    <div class="back-brand">EMBER</div>
  </section>
</body>
</html>
```